Powepoint Templates From Logo

We need 3 Powerpoint templates for use in a variety of presentations we develop and customize. Primary uses of the powerpoint presentations are for printed "pitch books" describing our firm's capabilities and approach (a lot of words with some design elements that we have developed), printed presentations of the results of financial evaluations of our clients (lots of charts and graphs) and as the talking points for speeches.

The design needs to be professional and "solid" to establish that we are capable of selling your multi-million dollar business, but also be a little different to show that we are not just boring MBA's.

Our current website and other materials have been developed internally and leave a great deal to be desired. I have initiated this project to demonstrate how much our look can be improved and, if successful, I hope to do much bigger projects in the future.
Updates

This is my first project and I thaank you all for your participation. Since I am new to this, I don;t know if I am providing the help and feedback as I should. Please feel free to let me know how I can be a better customer.

Target Market(s)

professionals (lawyers, accountaants), business owners, business groups, technology people

Industry/Entity Type

Financial

Requirements
Must have
• our logo
a place where logo of client can be inserted if appropriate
templates for the following pages
title page
standard bullet narrative page
page for charts and graphs to mostly fill the page
Should not have a lot of dark solid color that has to be printed.

Nice to have
• something to perk up the color a little

```html
<!DOCTYPE html>
<html lang="en">
<head>
<meta charset="utf-8">
<title>Project Title Here</title>
<link rel="stylesheet" href="https://fonts.googleapis.com/css2?family=Oswald:wght@700&family=Arimo:wght@400;700&display=swap">
<style>
  :root {
    --navy: #0b2b5a;
    --sky: #c6daf3;
    --sky-soft: #e9f1fb;
    --sub-blue: #8db3e2;
    --ink: #111111;
    --white: #ffffff;
  }
  * { margin: 0; padding: 0; box-sizing: border-box; }
  html, body { width: 1200px; height: 900px; overflow: hidden; background: var(--white); }
  .slide {
    position: relative;
    width: 1200px;
    height: 900px;
    overflow: hidden;
    background: var(--white);
    font-family: "Arimo", Arial, sans-serif;
  }
  .frame { position: absolute; inset: 0; width: 1200px; height: 900px; }
  .slide-title {
    position: absolute;
    right: 24px;
    top: 40px;
    font-family: "Oswald", "Arial Narrow", sans-serif;
    font-weight: 700;
    font-size: 62px;
    line-height: 1;
    letter-spacing: 0.5px;
    color: var(--navy);
    text-transform: uppercase;
  }
  .subhead {
    position: absolute;
    left: 85px;
    top: 232px;
    font-weight: 700;
    font-size: 41px;
    line-height: 1;
    color: var(--sub-blue);
    text-transform: uppercase;
  }
  .points {
    position: absolute;
    left: 85px;
    top: 299px;
    list-style: none;
  }
  .points li {
    position: relative;
    padding-left: 29px;
    height: 56px;
    font-size: 23.5px;
    line-height: 32px;
    color: var(--ink);
  }
  .points li svg {
    position: absolute;
    left: 2px;
    top: 10px;
    width: 12px;
    height: 14px;
  }
  .brand {
    position: absolute;
    left: 32px;
    top: 802px;
    display: flex;
    flex-direction: column;
    gap: 6px;
  }
  .brand-name {
    font-weight: 700;
    font-size: 34px;
    line-height: 1;
    color: var(--navy);
    letter-spacing: 0.5px;
  }
  .brand-tagline {
    font-size: 11px;
    line-height: 1;
    color: var(--navy);
    letter-spacing: 0.6px;
    text-transform: uppercase;
  }
  .page-number {
    position: absolute;
    right: 14px;
    top: 866px;
    font-size: 22px;
    line-height: 1;
    color: var(--white);
  }
</style>
</head>
<body>
<main class="slide">
  <svg class="frame" viewBox="0 0 1200 900" aria-hidden="true">
    <polygon points="0,0 600,0 0,178" fill="var(--sky)"/>
    <polygon points="0,0 578,0 0,166" fill="var(--navy)"/>
    <line x1="270" y1="99" x2="1200" y2="99" stroke="var(--sky)" stroke-width="2"/>
    <line x1="0" y1="760" x2="1200" y2="760" stroke="var(--sky)" stroke-width="2"/>
    <rect x="0" y="882" width="1200" height="18" fill="var(--sky-soft)"/>
    <polygon points="1200,792 1200,802 915,900 878,900" fill="var(--sky)"/>
    <polygon points="1200,802 1200,900 915,900" fill="var(--navy)"/>
  </svg>

  <h1 class="slide-title">Project Title Here</h1>

  <h2 class="subhead">Sub Text Here</h2>

  <ul class="points">
    <li><svg viewBox="0 0 12 14"><polyline points="3,2 9,7 3,12" fill="none" stroke="var(--navy)" stroke-width="3"/></svg>Lorem ipsum dolor sit ipsum, Lorem ipsum dolor sit ipsum</li>
    <li><svg viewBox="0 0 12 14"><polyline points="3,2 9,7 3,12" fill="none" stroke="var(--navy)" stroke-width="3"/></svg>Lorem ipsum dolor sit ipsum, Lorem ipsum dolor sit ipsum</li>
    <li><svg viewBox="0 0 12 14"><polyline points="3,2 9,7 3,12" fill="none" stroke="var(--navy)" stroke-width="3"/></svg>Lorem ipsum dolor sit ipsum Lorem ipsum dolor sit ipsum</li>
    <li><svg viewBox="0 0 12 14"><polyline points="3,2 9,7 3,12" fill="none" stroke="var(--navy)" stroke-width="3"/></svg>Lorem ipsum dolor sit ipsum, Lorem ipsum dolor sit ipsum</li>
    <li><svg viewBox="0 0 12 14"><polyline points="3,2 9,7 3,12" fill="none" stroke="var(--navy)" stroke-width="3"/></svg>Lorem ipsum dolor sit ipsum, Lorem ipsum dolor sit ipsum</li>
    <li><svg viewBox="0 0 12 14"><polyline points="3,2 9,7 3,12" fill="none" stroke="var(--navy)" stroke-width="3"/></svg>Lorem ipsum dolor sit ipsum Lorem ipsum dolor sit ipsum</li>
  </ul>

  <div class="brand">
    <span class="brand-name">HALDEN CAPITAL</span>
    <span class="brand-tagline">Business Sale • Valuation • Advisory</span>
  </div>

  <div class="page-number">PAGE 2 OF 2</div>
</main>
</body>
</html>
```